Brindle School of Music Website Design

Brindle School of Music would like to have a website designed. They are a new business similar to Halvern (https://halvernmusic.example).

We prefer using Adobe Fonts throughout the design. Kepler was used for the logo. Lorem Ipsum is fine to use except for headers.

Please keep track of any images/icons that are used in your design. We plan on purchasing the images used in the winning design.

Target Market(s)

Children age 10 - 18

Number of Pages Required

1 page

Font styles to use
Sans Serif

Colors
0054AA
0677BA
7BADD7
CADEEF
E8F1F8

```html
<!DOCTYPE html>
<html lang="en">
<head>
<meta charset="utf-8">
<title>Brindle School of Music</title>
<link rel="stylesheet" href="https://fonts.googleapis.com/css2?family=Playfair+Display:wght@700;800&family=Source+Sans+3:wght@400;600;700&display=swap">
<style>
:root{
  --navy:#0054AA;
  --blue:#0677BA;
  --sky:#7BADD7;
  --pale:#CADEEF;
  --mist:#E8F1F8;
  --ink:#3a3a3a;
  --white:#ffffff;
  --serif:"Playfair Display", Georgia, serif;
  --sans:"Source Sans 3", Arial, sans-serif;
}
*{box-sizing:border-box;margin:0;padding:0}
html,body{width:1200px;height:3800px;overflow:hidden;background:var(--white);font-family:var(--sans);color:var(--ink)}
.page{position:relative;width:1200px;height:3800px}
.abs{position:absolute}

/* top bar */
.topbar{left:0;top:0;width:1200px;height:56px;background:var(--mist)}
.topbar .icons{left:696px;top:20px;display:flex;gap:22px}
.topbtn{top:0;height:56px;width:168px;color:var(--white);font-family:var(--serif);font-size:17px;display:flex;align-items:center;justify-content:center;letter-spacing:.5px}
.topbtn.register{left:790px;background:var(--blue)}
.topbtn.donate{left:959px;background:var(--navy)}

/* nav */
.brand{left:74px;top:70px;width:120px;color:var(--navy);font-family:var(--serif);font-weight:700;font-size:19px;line-height:22px;text-align:center;display:flex;flex-direction:column;align-items:center;gap:6px}
.brand .mark{width:18px;height:18px;background:var(--navy)}
.nav{top:100px;left:252px;right:74px;display:flex;justify-content:space-between;font-family:var(--serif);font-size:13.5px;letter-spacing:.4px;color:var(--ink)}
.nav .active{color:var(--blue)}

/* hero */
.hero{left:0;top:155px;width:1200px;height:655px;background:linear-gradient(120deg,#8a6a5d 0%,#5a4a44 40%,#7d6455 70%,#a99182 100%)}
.hero-title{left:0;width:1200px;top:410px;text-align:center;color:var(--white);font-family:var(--serif);font-size:74px;font-weight:700;letter-spacing:-1px}
.hero-sub{left:240px;width:720px;top:493px;text-align:center;color:var(--white);font-size:27px;font-weight:600;line-height:38px}
.btn{height:56px;width:167px;display:flex;align-items:center;justify-content:center;color:var(--white);font-family:var(--serif);font-size:17px;letter-spacing:.5px}
.hero .dots{}
.dot{top:763px;width:11px;height:11px;border-radius:50%;background:var(--white)}

/* section heads */
.h2{font-family:var(--serif);font-weight:700;font-size:36px;color:var(--ink);letter-spacing:.3px}

/* programs */
.prog-card{background:var(--pale);border-radius:18px;width:242px;height:225px;text-align:center}
.prog-title{color:var(--navy);font-weight:700;font-size:18.5px;letter-spacing:.3px}
.prog-text{font-size:16.5px;line-height:27px;color:var(--ink)}
.photo-circle{border-radius:50%;border:6px solid var(--white);width:200px;height:200px}

/* welcome */
.welcome-photo{left:0;top:1405px;width:1200px;height:518px;background:linear-gradient(135deg,#b48f77,#6e6a6c 45%,#4b4a52)}
.welcome-copy{left:616px;top:1470px;width:520px;color:var(--white)}
.welcome-copy h2{font-family:var(--serif);font-weight:700;font-size:37px;line-height:47px;letter-spacing:.3px}
.welcome-copy p{margin-top:26px;font-size:16px;line-height:26.8px}
.btn-outline{left:616px;top:1795px;width:164px;height:52px;background:var(--white);color:var(--blue);font-family:var(--serif);font-size:17px;display:flex;align-items:center;justify-content:center}

/* arrows */
.arrow{width:30px;height:30px}

/* testimonials */
.quote-text{font-size:16.3px;line-height:26.8px;color:var(--ink)}
.quote-mark{font-family:var(--serif);font-size:150px;line-height:1;color:var(--pale)}
.quote-name{font-weight:700;font-size:16.5px;color:var(--navy);letter-spacing:.6px}
.avatar{width:92px;height:92px;border-radius:50%;border:4px solid var(--white)}

/* stats */
.stats{left:0;top:2456px;width:1200px;height:368px;background:linear-gradient(110deg,#0b4a92,#0a3f80 40%,#0d56a8 100%)}
.stat{top:2520px;width:260px;text-align:center;color:var(--white)}
.stat .num{font-weight:700;font-size:43px;line-height:50px;margin-top:32px}
.stat .lbl{font-weight:600;font-size:18px;line-height:24px}
.stat svg{display:block;margin:0 auto}

/* news */
.news-img{top:2967px;width:329px;height:217px;border-radius:6px}
.news-title{top:3212px;width:330px;color:var(--blue);font-weight:600;font-size:23px;line-height:27px}
.news-text{top:3281px;width:320px;font-size:16px;line-height:25px;color:var(--ink)}

/* footer */
.footer{left:0;top:3418px;width:1200px;height:321px;background:var(--pale)}
.footer-brand{left:74px;top:3560px;width:217px;text-align:center;color:var(--navy);font-family:var(--serif);font-weight:700;font-size:34px;line-height:40px;display:flex;flex-direction:column;align-items:center;gap:10px}
.footer-brand .mark{width:26px;height:26px;background:var(--navy)}
.fcol{top:3484px}
.fcol h4{font-weight:700;font-size:17px;color:var(--navy);letter-spacing:.3px;margin-bottom:6px}
.fcol li{list-style:none;font-size:14px;line-height:29px;color:var(--ink)}
.contact-row{display:flex;gap:14px;font-size:14px;line-height:21px;margin-bottom:11px}
.contact-row svg{flex:none;margin-top:3px}
.social{top:3660px;left:884px;display:flex;gap:24px}
.social span{width:22px;height:22px;border-radius:50%;background:var(--navy)}
.copybar{left:0;top:3739px;width:1200px;height:61px;background:var(--sky);color:var(--white);font-size:15px;display:flex;align-items:center;justify-content:center}
</style>
</head>
<body>
<div class="page">

  <!-- top bar -->
  <div class="abs topbar"></div>
  <div class="abs topbar icons" style="background:none;width:auto;height:auto;left:696px;top:20px">
    <svg width="16" height="16" viewBox="0 0 16 16"><circle cx="6.5" cy="6.5" r="4.8" fill="none" stroke="#666" stroke-width="2"/><line x1="10" y1="10" x2="14.5" y2="14.5" stroke="#666" stroke-width="2.4"/></svg>
    <svg width="16" height="16" viewBox="0 0 16 16"><circle cx="8" cy="5" r="3.6" fill="#666"/><path d="M1.5 15c0-4 3-6 6.5-6s6.5 2 6.5 6z" fill="#666"/></svg>
  </div>
  <div class="abs topbtn register">REGISTER</div>
  <div class="abs topbtn donate">DONATE</div>

  <!-- nav -->
  <div class="abs brand"><span class="mark"></span><span>Brindle School of Music</span></div>
  <nav class="abs nav">
    <span class="active">HOME</span><span>OUR PROGRAMS</span><span>ABOUT US</span><span>OUR IMPACT</span><span>SUPPORT</span><span>STUDENT RESOURCES</span><span>CONTACT US</span>
  </nav>

  <!-- hero -->
  <div class="abs hero" role="img" aria-label="Photo of three children playing flute, guitar and violin together"></div>
  <h1 class="abs hero-title">BRINDLE SCHOOL OF MUSIC</h1>
  <p class="abs hero-sub">Acepteur sint occaecat cupidatat non proident, sunt in culpa qui officia deserunt mollit.</p>
  <div class="abs btn" style="left:421px;top:576px;background:var(--blue)">REGISTER</div>
  <div class="abs btn" style="left:617px;top:576px;background:var(--navy)">DONATE</div>
  <span class="abs dot" style="left:562px"></span>
  <span class="abs dot" style="left:585px"></span>
  <span class="abs dot" style="left:608px"></span>
  <span class="abs dot" style="left:631px"></span>

  <!-- programs -->
  <h2 class="abs h2" style="left:0;width:1200px;text-align:center;top:882px">OUR PROGRAMS</h2>

  <div class="abs prog-card" style="left:74px;top:1092px">
    <div class="prog-title" style="margin-top:121px">EARLY CHILDHOOD</div>
    <div class="prog-text" style="margin-top:6px">Sed ut perspiciatis unde<br>omnis iste</div>
  </div>
  <div class="abs photo-circle" role="img" aria-label="Photo of young children playing a xylophone" style="left:96px;top:985px;background:linear-gradient(135deg,#e9dccf,#d59a6a 50%,#7aa7b5)"></div>

  <div class="abs prog-card" style="left:345px;top:983px">
    <div class="prog-title" style="margin-top:27px">PRIVATE LESSONS</div>
    <div class="prog-text" style="margin-top:6px">Sed ut perspiciatis unde<br>omnis iste</div>
  </div>
  <div class="abs photo-circle" role="img" aria-label="Photo of a student at a piano lesson" style="left:366px;top:1113px;background:linear-gradient(135deg,#7a5a4a,#3a2a24 50%,#c9a58a)"></div>

  <div class="abs prog-card" style="left:614px;top:1092px">
    <div class="prog-title" style="margin-top:121px">GROUP LESSONS</div>
    <div class="prog-text" style="margin-top:6px">Sed ut perspiciatis unde<br>omnis iste</div>
  </div>
  <div class="abs photo-circle" role="img" aria-label="Photo of a group lesson with music stands" style="left:637px;top:985px;background:linear-gradient(135deg,#d9d9d9,#8b8f96 50%,#3a3f4a)"></div>

  <div class="abs prog-card" style="left:886px;top:983px">
    <div class="prog-title" style="margin-top:27px">SUMMER CAMPS</div>
    <div class="prog-text" style="margin-top:6px">Sed ut perspiciatis unde<br>omnis iste</div>
  </div>
  <div class="abs photo-circle" role="img" aria-label="Photo of children with tambourines at summer camp" style="left:905px;top:1113px;background:linear-gradient(135deg,#9cc46a,#4e6f8a 50%,#c49a74)"></div>

  <!-- welcome -->
  <div class="abs welcome-photo" role="img" aria-label="Photo of a school band with keyboard, violin, clarinet and trumpet"></div>
  <svg class="abs" style="left:0;top:1405px" width="1200" height="518" viewBox="0 0 1200 518">
    <defs><linearGradient id="wg" x1="0" y1="0" x2="1" y2="1"><stop offset="0" stop-color="#0677BA"/><stop offset="1" stop-color="#0054AA"/></linearGradient></defs>
    <path d="M615 0 C540 60 520 180 500 300 C485 400 450 470 415 518 L1200 518 L1200 0 Z" fill="url(#wg)"/>
  </svg>
  <div class="abs welcome-copy">
    <h2>WELCOME TO THE<br>BRINDLE SCHOOL OF MUSIC</h2>
    <p>Nemo enim ipsam voluptatem quia voluptas sit aspernatur aut odit aut fugit, sed quia consequuntur magni dolores eos qui ratione voluptatem sequi nesciunt eque porro quisquam est, qui dolorem ipsum quia dolor sit amet, consectetur, adipisci velit, sed quia non numquam eius modi tempora incidunt ut labore et dolore qui ratione voluptatem sequi nesciunt eque porro quisquam est, qui dolorem ipsum quia dolor sit amet, consectetur.</p>
  </div>
  <div class="abs btn-outline">READ MORE</div>

  <!-- testimonials -->
  <h2 class="abs h2" style="left:74px;top:1995px">TESTIMONIALS</h2>
  <svg class="abs arrow" style="left:1054px;top:2003px" viewBox="0 0 30 30"><circle cx="15" cy="15" r="15" fill="#7BADD7"/><path d="M17 8 L10 15 L17 22 M10 15 H22" stroke="#fff" stroke-width="3" fill="none" stroke-linecap="round" stroke-linejoin="round"/></svg>
  <svg class="abs arrow" style="left:1097px;top:2003px" viewBox="0 0 30 30"><circle cx="15" cy="15" r="15" fill="#0054AA"/><path d="M13 8 L20 15 L13 22 M20 15 H8" stroke="#fff" stroke-width="3" fill="none" stroke-linecap="round" stroke-linejoin="round"/></svg>

  <svg class="abs" style="left:74px;top:2071px" width="512" height="290" viewBox="0 0 512 290"><path d="M18 0 H494 Q512 0 512 18 V240 Q512 250 500 252 L18 288 Q0 290 0 272 V18 Q0 0 18 0Z" fill="#E8F1F8"/></svg>
  <div class="abs quote-mark" style="left:90px;top:2050px">&ldquo;</div>
  <p class="abs quote-text" style="left:108px;top:2115px;width:450px">Nemo enim ipsam voluptatem quia voluptas sit aspernatur aut odit aut fugit, sed quia consequuntur magni dolores eos qui ratione voluptatem sequi nesciunt eque porro quisquam est, qui dolorem ipsum quia dolor sit amet, consectetur, adipisci velit, sed quia non numquam eius modi tempora incidunt ut labore et dolore..&rdquo;</p>
  <div class="abs quote-name" style="left:108px;top:2286px">NAME&nbsp; HEADING</div>
  <div class="abs avatar" role="img" aria-label="Portrait photo of a parent" style="left:460px;top:2279px;background:linear-gradient(135deg,#e7cfa0,#c79a7a)"></div>

  <svg class="abs" style="left:614px;top:2071px" width="512" height="290" viewBox="0 0 512 290"><path d="M18 0 H494 Q512 0 512 18 V240 Q512 250 500 252 L18 288 Q0 290 0 272 V18 Q0 0 18 0Z" fill="#E8F1F8"/></svg>
  <div class="abs quote-mark" style="left:630px;top:2050px">&ldquo;</div>
  <p class="abs quote-text" style="left:648px;top:2115px;width:450px">Nemo enim ipsam voluptatem quia voluptas sit aspernatur aut odit aut fugit, sed quia consequuntur magni dolores eos qui ratione voluptatem sequi nesciunt eque porro quisquam est, qui dolorem ipsum quia dolor sit amet, consectetur, adipisci velit, sed quia non numquam eius modi tempora incidunt ut labore et dolore..&rdquo;</p>
  <div class="abs quote-name" style="left:648px;top:2286px">NAME&nbsp; HEADING</div>
  <div class="abs avatar" role="img" aria-label="Portrait photo of a student with a violin" style="left:1000px;top:2279px;background:linear-gradient(135deg,#d8d8d8,#5a4a44)"></div>

  <!-- stats -->
  <div class="abs stats" role="img" aria-label="Background photo of a student playing saxophone, tinted blue"></div>
  <div class="abs stat" style="left:66px">
    <svg width="80" height="88" viewBox="0 0 80 88"><text x="40" y="80" text-anchor="middle" font-family="Source Sans 3, Arial, sans-serif" font-weight="700" font-size="100" fill="#fff">$</text></svg>
    <div class="num">$1.4 Million</div><div class="lbl">Excepteur sint occaecat<br>cupidatat non</div>
  </div>
  <div class="abs stat" style="left:333px">
    <svg width="110" height="88" viewBox="0 0 110 88"><polygon points="55,12 108,34 55,56 2,34" fill="#fff"/><path d="M28 46 V66 Q55 80 82 66 V46 L55 58 Z" fill="#fff"/><line x1="14" y1="38" x2="14" y2="70" stroke="#fff" stroke-width="3"/><rect x="10" y="68" width="8" height="14" fill="#fff"/></svg>
    <div class="num">38</div><div class="lbl">Excepteur sint occaecat<br>cupidatat non</div>
  </div>
  <div class="abs stat" style="left:607px">
    <svg width="80" height="88" viewBox="0 0 80 88"><rect x="14" y="0" width="52" height="88" rx="4" fill="#fff"/><g fill="#0a3f80"><rect x="24" y="10" width="10" height="10"/><rect x="46" y="10" width="10" height="10"/><rect x="24" y="30" width="10" height="10"/><rect x="46" y="30" width="10" height="10"/><rect x="24" y="50" width="10" height="10"/><rect x="46" y="50" width="10" height="10"/><rect x="34" y="70" width="12" height="18"/></g></svg>
    <div class="num">46%</div><div class="lbl">Excepteur sint occaecat<br>cupidatat non</div>
  </div>
  <div class="abs stat" style="left:875px">
    <svg width="90" height="88" viewBox="0 0 90 88"><path d="M26 16 L82 2 V66" stroke="#fff" stroke-width="10" fill="none"/><rect x="26" y="16" width="10" height="54" fill="#fff"/><ellipse cx="20" cy="72" rx="17" ry="13" fill="#fff"/><ellipse cx="66" cy="66" rx="17" ry="13" fill="#fff"/></svg>
    <div class="num">64%</div><div class="lbl">Excepteur sint occaecat<br>cupidatat non</div>
  </div>

  <!-- news -->
  <h2 class="abs h2" style="left:74px;top:2892px">NEWS UPDATE</h2>
  <svg class="abs arrow" style="left:1054px;top:2900px" viewBox="0 0 30 30"><circle cx="15" cy="15" r="15" fill="#7BADD7"/><path d="M17 8 L10 15 L17 22 M10 15 H22" stroke="#fff" stroke-width="3" fill="none" stroke-linecap="round" stroke-linejoin="round"/></svg>
  <svg class="abs arrow" style="left:1097px;top:2900px" viewBox="0 0 30 30"><circle cx="15" cy="15" r="15" fill="#0054AA"/><path d="M13 8 L20 15 L13 22 M20 15 H8" stroke="#fff" stroke-width="3" fill="none" stroke-linecap="round" stroke-linejoin="round"/></svg>

  <div class="abs news-img" role="img" aria-label="Photo of an ensemble rehearsal with music stands" style="left:74px;background:linear-gradient(135deg,#e4e0da,#8a8f9a 50%,#3d3b45)"></div>
  <div class="abs news-img" role="img" aria-label="Photo of a smiling boy playing acoustic guitar" style="left:436px;background:linear-gradient(135deg,#d9c8b0,#a77a52 50%,#5b4a6a)"></div>
  <div class="abs news-img" role="img" aria-label="Photo of a student singing with band members" style="left:797px;background:linear-gradient(135deg,#f0ece6,#9a8e86 50%,#3a3436)"></div>

  <div class="abs news-title" style="left:74px">Nemo enim ipsam voluptatem quia voluptas sit aspe.</div>
  <div class="abs news-title" style="left:436px">Nemo enim ipsam voluptatem quia voluptas sit aspe.</div>
  <div class="abs news-title" style="left:797px">Nemo enim ipsam voluptatem quia voluptas sit aspe.</div>
  <p class="abs news-text" style="left:74px">Sed quia consequuntur magni dolores eos qui ratione voluptatem sequi nesciunt sed do eiusmod tempor incidi...</p>
  <p class="abs news-text" style="left:436px">Sed quia consequuntur magni dolores eos qui ratione voluptatem sequi nesciunt sed do eiusmod tempor incidi...</p>
  <p class="abs news-text" style="left:797px">Sed quia consequuntur magni dolores eos qui ratione voluptatem sequi nesciunt sed do eiusmod tempor incidi...</p>

  <!-- footer -->
  <footer class="abs footer"></footer>
  <div class="abs footer-brand"><span class="mark"></span><span>Brindle School of Music</span></div>

  <div class="abs fcol" style="left:342px">
    <h4>SITE MAP</h4>
    <ul><li>Home</li><li>Our Programs</li><li>About Us</li><li>Our Impact</li><li>Support</li><li>Student Resources</li><li>Contact Us</li></ul>
  </div>
  <div class="abs fcol" style="left:577px">
    <h4>STUDENT RESOURCES</h4>
    <ul><li>Excepteur sint</li><li>Occaecat cupidatat</li><li>Non proident</li><li>Sunt in culpa qui</li><li>Officia deserunt mollit</li><li>Anim id est</li></ul>
  </div>
  <div class="abs fcol" style="left:884px;width:240px">
    <h4>CONTACT ADDRESS</h4>
    <div class="contact-row" style="margin-top:8px">
      <svg width="16" height="14" viewBox="0 0 16 14"><path d="M0 2 L5 0 L11 2 L16 0 V12 L11 14 L5 12 L0 14Z" fill="#0054AA"/></svg>
      <span>Excepteur sint occaecat<br>cupidatat non pr</span>
    </div>
    <div class="contact-row">
      <svg width="16" height="14" viewBox="0 0 16 14"><path d="M3 1 L6 1 L7 4 L5 5 Q6 8 9 9 L10 7 L13 8 L13 11 Q13 13 11 13 Q2 12 1 3 Q1 1 3 1Z" fill="#0054AA"/></svg>
      <span>1-800-555-0142</span>
    </div>
    <div class="contact-row">
      <svg width="16" height="14" viewBox="0 0 16 14"><rect x="0" y="2" width="16" height="11" rx="1" fill="#0054AA"/><path d="M1 3 L8 8 L15 3" stroke="#CADEEF" stroke-width="1.4" fill="none"/></svg>
      <span>hello@brindlemusic.example</span>
    </div>
  </div>
  <div class="abs social"><span></span><span></span><span></span><span></span><span></span></div>

  <div class="abs copybar">Copyright &copy; 2023. Company Name&nbsp; All Rights Reserved</div>
</div>
</body>
</html>
```